Create a professional, fresh and polished oversized post card for law firm specializing in Estate Planning & Probate Law for High Net Worth Clients

Use any picture(s) of your choice (mine or ones you recommend), logo, headshot and company info

www.morvenashcroftlaw.com

Westgate Office - 4100 Birchmont Road, Suite 1500, Charlotte, NC 28214
Kerrington Office - 13480 Oakridge Lane, Suite 300, Charlotte, NC 28269

Phone (704) 555-0187

Use this card for a Free Consultation

Target Market(s)

young and old families too; business owners

Industry/Entity Type

Law Firm

Font styles to use
Serif
Sans Serif

Requirements
Must have
• Use any picture(s) of your choice (mine or ones you recommend), logo, headshot and company info
• www.morvenashcroftlaw.com
• Westgate Office - 4100 Birchmont Road, Suite 1500, Charlotte, NC 28214
• Kerrington Office - 13480 Oakridge Lane, Suite 300, Charlotte, NC 28269
• Phone (704) 555-0187
• Use this card for a Free Consultation
Nice to have
• great colors and great design; like graphics with depth /shading
Should not have
• don't use too many pics - keep it simple

```html
<!DOCTYPE html>
<html lang="en">
<head>
<meta charset="utf-8">
<title>Morven Ashcroft Law – Postcard</title>
<link rel="stylesheet" href="https://fonts.googleapis.com/css2?family=Ubuntu:wght@400;500&family=Raleway:wght@300;400&family=Cabin:wght@400&family=Crimson+Text:ital@0;1&display=swap">
<style>
  :root {
    --navy: #0c4462;
    --mid-blue: #17688e;
    --teal-text: #1b76a0;
    --light-box: #e4ecf3;
    --grey-text: #6e6e6e;
    --ink: #2b2b2b;
    --page: #ecebe8;
    --white: #ffffff;
  }
  * { margin: 0; padding: 0; box-sizing: border-box; }
  html, body { width: 904px; height: 1200px; overflow: hidden; background: var(--page); }
  .canvas { position: relative; width: 904px; height: 1200px; }

  .card { position: absolute; left: 48px; width: 808px; height: 524px; overflow: hidden;
          box-shadow: 0 3px 10px rgba(0,0,0,.18); }
  .card--front { top: 58px; background: #f3f8fb; }
  .card--back { top: 614px; background: var(--white); }
  .card svg.backdrop { position: absolute; inset: 0; }
  .abs { position: absolute; }

  /* front */
  .brand-mark { left: 0; top: 0; width: 280px; }
  .brand-name { position: absolute; font-family: "Ubuntu", sans-serif; font-weight: 400; color: var(--teal-text); white-space: nowrap; }
  .brand-sub { position: absolute; font-family: "Crimson Text", serif; color: var(--ink); letter-spacing: 1px; padding: 0 6px; }
  .rule { position: absolute; height: 1px; background: var(--ink); }
  .headline { left: 28px; top: 243px; font-family: "Raleway", sans-serif; font-weight: 400;
              font-size: 21.5px; line-height: 31px; color: var(--teal-text); }
  .intro { left: 28px; top: 352px; width: 289px; font-family: "Cabin", sans-serif; font-size: 11.2px;
           line-height: 19px; color: #3a3a3a; text-align: justify; }
  .front-phone { right: 28px; top: 62px; font-family: "Raleway", sans-serif; font-weight: 300;
                 font-size: 29px; color: var(--grey-text); letter-spacing: .5px; }
  .offer { right: 36px; top: 426px; font-family: "Crimson Text", serif; font-style: italic; font-size: 12.5px; color: var(--white); }
  .front-web { left: 494px; top: 454px; width: 284px; font-family: "Raleway", sans-serif; font-size: 18px; letter-spacing: 1px; color: var(--white); white-space: nowrap; }
  .front-email { left: 494px; top: 493px; width: 284px; font-family: "Raleway", sans-serif; font-size: 11.5px; letter-spacing: 2.9px; color: var(--white); white-space: nowrap; }
  .front-divider { left: 494px; top: 487px; width: 284px; height: 1px; background: rgba(255,255,255,.55); }

  /* back */
  .office-panel { left: 40px; top: 2px; width: 265px; height: 211px; background: var(--mid-blue); }
  .office { position: absolute; left: 0; width: 100%; text-align: center; color: var(--white); }
  .office h2 { font-family: "Ubuntu", sans-serif; font-weight: 500; font-size: 22px; margin-bottom: 6px; }
  .office p { font-family: "Cabin", sans-serif; font-size: 15.5px; line-height: 21px; }
  .office-split { position: absolute; left: 0; top: 115px; width: 100%; height: 3px; background: var(--white); }
  .services { left: 36px; top: 226px; width: 275px; list-style: none; }
  .services li { font-family: "Raleway", sans-serif; font-size: 18px; color: var(--white); text-align: center;
                 height: 33px; line-height: 31px; border-bottom: 1px solid rgba(255,255,255,.85); }
  .services li:last-child { border-bottom: none; }
  .back-web { left: 24px; width: 290px; top: 474px; text-align: center; font-family: "Raleway", sans-serif;
              font-size: 17px; letter-spacing: 1.4px; color: var(--white); white-space: nowrap; }
  .tagline { left: 388px; top: 118px; font-family: "Crimson Text", serif; font-size: 11.5px; letter-spacing: 1px; color: var(--teal-text); }
  .box { position: absolute; background: var(--light-box); font-family: Arial, Helvetica, sans-serif; font-size: 15px; color: #111; text-align: center; }
  .headshot { left: 382px; top: 237px; width: 126px; height: 153px; border: 4px solid var(--navy);
              background: linear-gradient(160deg, #c9c2b4 0%, #b79f7a 45%, #2c2f38 100%); }
  .contact { left: 350px; width: 188px; text-align: center; font-family: "Cabin", sans-serif; color: var(--navy); white-space: nowrap; }
</style>
</head>
<body>
<main class="canvas">

  <!-- Front side -->
  <section class="card card--front">
    <svg class="backdrop" width="808" height="524" viewBox="0 0 808 524">
      <defs>
        <linearGradient id="photoTone" x1="0" y1="0" x2="1" y2="0">
          <stop offset="0" stop-color="#f3f8fb" stop-opacity="0"/>
          <stop offset=".25" stop-color="#d9c3a7"/>
          <stop offset=".6" stop-color="#c7b09a"/>
          <stop offset="1" stop-color="#9fb7c6"/>
        </linearGradient>
        <linearGradient id="band" x1="0" y1="0" x2="1" y2="0">
          <stop offset="0" stop-color="#1d86b4"/>
          <stop offset="1" stop-color="#0c4462"/>
        </linearGradient>
        <radialGradient id="badge" cx=".5" cy=".4" r=".6">
          <stop offset="0" stop-color="#2a86b3"/>
          <stop offset="1" stop-color="#0c4462"/>
        </radialGradient>
      </defs>
      <rect x="300" y="42" width="508" height="420" fill="url(#photoTone)" role="img" aria-label="Photo of a smiling three-generation family on a beach"/>
      <rect x="0" y="0" width="808" height="42" fill="url(#band)"/>
      <polygon points="180,0 240,0 190,42 130,42" fill="#2a97c4" opacity=".45"/>
      <polygon points="300,0 540,0 490,42 250,42" fill="#1c7fae" opacity=".45"/>
      <polygon points="0,466 0,524 150,524" fill="#c9c4be"/>
      <polygon points="120,524 808,374 808,524" fill="var(--navy)"/>
      <polygon points="120,524 808,374 808,379 150,524" fill="#7f9aaa" opacity=".6"/>
      <circle cx="418" cy="461" r="54" fill="var(--navy)"/>
      <circle cx="418" cy="461" r="47" fill="var(--white)"/>
      <circle cx="418" cy="461" r="39" fill="url(#badge)"/>
    </svg>

    <div class="abs brand-mark">
      <svg class="abs" style="left:102px;top:56px" width="76" height="76" viewBox="0 0 76 76">
        <circle cx="38" cy="38" r="37" fill="var(--navy)"/>
      </svg>
      <div class="rule" style="left:28px;top:142px;width:225px"></div>
      <div class="brand-name" style="left:28px;top:148px;width:225px;text-align:center;font-size:27px">Morven Ashcroft</div>
      <div class="rule" style="left:28px;top:203px;width:70px"></div>
      <div class="rule" style="left:183px;top:203px;width:70px"></div>
      <div class="brand-sub" style="left:99px;top:193px;font-size:14px">LAW PLLC</div>
    </div>

    <h1 class="abs headline">SERVING CLIENTS WITH<br>COMPASSION AND LEGAL<br>GUIDANCE IS OUR PASSION...</h1>
    <p class="abs intro">Morven Ashcroft Law, PLLC serving clients in estate planning, estate administration, probate law, wills, revocable trusts, irrevocable trusts, powers of attorney, health care powers of attorney, living wills, hipaa releases, guardianships, special needs planning, wealth transfers, elder law and business law in North Carolina and South Carolina.</p>

    <div class="abs front-phone">(704) 555-0187</div>
    <div class="abs offer">Use this card for a Free Consultation</div>
    <div class="abs front-web">www.morvenashcroftlaw.com</div>
    <div class="abs front-divider"></div>
    <div class="abs front-email">morven@morvenashcroftlaw.com</div>
  </section>

  <!-- Back side -->
  <section class="card card--back">
    <svg class="backdrop" width="808" height="524" viewBox="0 0 808 524">
      <rect x="0" y="0" width="338" height="524" fill="var(--navy)"/>
    </svg>

    <div class="abs office-panel">
      <div class="office" style="top:24px">
        <h2>Westgate Office</h2>
        <p>4100 Birchmont Road, Suite 1500,<br>Charlotte, NC 28214</p>
      </div>
      <div class="office-split"></div>
      <div class="office" style="top:128px">
        <h2>Kerrington Office</h2>
        <p>13480 Oakridge Lane, Suite 300,<br>Charlotte, NC 28269</p>
      </div>
    </div>

    <ul class="abs services">
      <li>Estate Administration</li>
      <li>Probate Law</li>
      <li>Estate Planning</li>
      <li>Wills</li>
      <li>Trusts</li>
      <li>Living Wills</li>
      <li>Healthcare Powers</li>
    </ul>
    <div class="abs back-web">www.morvenashcroftlaw.com</div>

    <div class="rule" style="left:388px;top:33px;width:230px"></div>
    <div class="brand-name" style="left:388px;top:44px;width:230px;text-align:center;font-size:26px">Morven Ashcroft</div>
    <div class="rule" style="left:388px;top:96px;width:74px"></div>
    <div class="rule" style="left:544px;top:96px;width:74px"></div>
    <div class="brand-sub" style="left:461px;top:86px;font-size:14px">LAW PLLC</div>
    <div class="abs tagline">BIG THINGS START FROM LITTLE IDEAS</div>

    <div class="box" style="left:680px;top:13px;width:116px;height:117px;padding-top:38px">Postage<br>Area</div>
    <div class="box" style="left:538px;top:230px;width:258px;height:230px;padding-top:42px">Address Area</div>
    <div class="box" style="left:351px;top:450px;width:445px;height:62px;padding-top:22px">Barcode Area</div>

    <div class="abs headshot" role="img" aria-label="Headshot of the attorney"></div>
    <div class="abs contact" style="top:404px;font-size:13px">morven@morvenashcroftlaw.com</div>
    <div class="abs contact" style="top:422px;font-size:16px;font-weight:500;font-family:'Ubuntu',sans-serif">(704) 555-0187</div>
  </section>

</main>
</body>
</html>
```